Electrical business card

I require a business card for my company I will attach my log. My business is a electrical business. I would like the card to have a smart corporate look nothing to over the top.

Industry/Entity Type

Business

```html
<!DOCTYPE html>
<html lang="en">
<head>
<meta charset="UTF-8">
<title>Kelvaro Solutions – Business Card</title>
<link href="https://fonts.googleapis.com/css2?family=Oswald:wght@500;600&family=Roboto+Condensed:wght@400;700&display=swap" rel="stylesheet">
<style>
  :root {
    --page-bg: #2a2a2a;
    --card-black: #050505;
    --accent-blue: #29a8e0;
    --text-white: #ffffff;
    --logo-grey: #b9bcbf;
    --band-dark: #1a1a1a;
    --band-light: #4a4a4a;
  }
  * { margin: 0; padding: 0; box-sizing: border-box; }
  html, body { width: 900px; height: 1200px; overflow: hidden; background: var(--page-bg); }
  .canvas { position: relative; width: 900px; height: 1200px; }

  .card {
    position: absolute; left: 66px; width: 720px;
    background: var(--card-black);
    box-shadow: 0 8px 24px rgba(0,0,0,.6);
    overflow: hidden;
  }
  .card--front { top: 120px; height: 444px; }
  .card--back  { top: 585px; height: 585px; }

  .holder { position: absolute; top: 22px; width: 100%; text-align: center; }
  .holder__name {
    font-family: "Oswald", sans-serif; font-weight: 600;
    font-size: 38px; line-height: 1.2; color: var(--text-white); letter-spacing: 1px;
  }
  .holder__position {
    font-family: "Oswald", sans-serif; font-weight: 500;
    font-size: 20px; line-height: 1.2; color: var(--accent-blue);
  }

  .rule { position: absolute; left: 0; width: 100%; height: 4px; background: var(--accent-blue); }

  .contacts {
    position: absolute; display: grid; grid-template-columns: auto auto;
    column-gap: 6px;
    font-family: "Roboto Condensed", sans-serif;
  }
  .contacts dt { color: var(--text-white); font-weight: 700; text-align: right; }
  .contacts dd { color: var(--accent-blue); font-weight: 400; }
  .contacts--main { left: 40px; top: 192px; font-size: 25px; line-height: 38px; }
  .contacts--office { left: 440px; top: 186px; font-size: 17px; line-height: 29px; }

  .logo-band {
    position: absolute; left: 0; width: 100%;
    background: linear-gradient(90deg, var(--band-dark) 0%, var(--band-light) 45%, var(--band-light) 58%, var(--band-dark) 100%);
    display: flex; align-items: center; justify-content: center;
  }
  .card--front .logo-band { top: 336px; height: 94px; gap: 16px; }
  .card--back  .logo-band { top: 159px; height: 133px; gap: 22px; }

  .brand__dot { border-radius: 50%; background: var(--accent-blue); flex: none; }
  .card--front .brand__dot { width: 38px; height: 38px; }
  .card--back  .brand__dot { width: 52px; height: 52px; }

  .brand__text { font-family: "Oswald", sans-serif; }
  .brand__name { font-weight: 500; color: var(--logo-grey); letter-spacing: 2px; line-height: 1.05; }
  .brand__tagline { font-weight: 500; color: var(--accent-blue); letter-spacing: 1.5px; line-height: 1.2; }
  .card--front .brand__name { font-size: 44px; }
  .card--front .brand__tagline { font-size: 15px; }
  .card--back .brand__name { font-size: 58px; }
  .card--back .brand__tagline { font-size: 20px; }
</style>
</head>
<body>
<main class="canvas">

  <section class="card card--front" aria-label="Business card front">
    <header class="holder">
      <h1 class="holder__name">CARD HOLDER NAME</h1>
      <p class="holder__position">POSITION</p>
    </header>
    <div class="rule" style="top:118px"></div>

    <dl class="contacts contacts--main">
      <dt>Phone:</dt><dd>555 010 4821</dd>
      <dt>Email:</dt><dd>info@kelvaro.com</dd>
      <dt>Fax:</dt><dd>555 010 4822</dd>
    </dl>

    <dl class="contacts contacts--office">
      <dt>Street:</dt><dd>12 Harbor Lane</dd>
      <dt>Phone:</dt><dd>555 010 4830</dd>
      <dt>Email:</dt><dd>office@kelvaro.com</dd>
      <dt>Fax:</dt><dd>555 010 4831</dd>
    </dl>

    <div class="rule" style="top:328px"></div>
    <div class="logo-band">
      <span class="brand__dot"></span>
      <div class="brand__text">
        <div class="brand__name">KELVARO SOLUTIONS</div>
        <div class="brand__tagline">ELECTRICAL CONTRACTORS</div>
      </div>
    </div>
    <div class="rule" style="top:434px"></div>
  </section>

  <section class="card card--back" aria-label="Business card back">
    <div class="rule" style="top:151px"></div>
    <div class="logo-band">
      <span class="brand__dot"></span>
      <div class="brand__text">
        <div class="brand__name">KELVARO SOLUTIONS</div>
        <div class="brand__tagline">ELECTRICAL CONTRACTORS</div>
      </div>
    </div>
    <div class="rule" style="top:296px"></div>
  </section>

</main>
</body>
</html>
```